Wordpress Design for Marcus Thornbury | Quiet Resolve

Summary
I am accepting designs concepts for my personal blog and web presence – http://www.marcusthornbury.example. The Blog, subtitled “Quiet Resolve”, provides a platform upon which I have established a personal brand and market my services as an board member, executive advisor, public speaker, and thought leader.
The successful design will balance an executive and professional design with a bit of innovation and passion. It will match the style and colors of the logo provided and adhere to the requirements listed below while providing a visually creative, appealing, and user-engaging experience.
A few blogs that I consider to be well designed and similar in content to what I’m looking for include:
• http://peterlangridge.example (by far the best representation)
• http://cabinwriter.example/
• http://www.brunocaldwell.example/
Technical Requirements
The design must be implementable in WordPress using “Plainframe Theme” (http://plainframetheme.example/). Customizations to Plainframe Theme are allowed, but should not be extraordinary.
The design must be implementable using clean and standard html/css techniques.
The design must include a standard header that leverages the attached logo
The design must include a search engine optimized footer layout that includes various links. The footer must include a series of small print links include a permission policy and a privacy policy.
The design must include placeholders for advertisements on each page. Any standard Google Adwords sizes are acceptable.
The design must include a standard site template/shell and at least 3 internal page designs.
Designs should be submitted for (at minimum) the following pages (detailed below):
• Home
• About
• Boards and/or Speaking pages
Information Architecture
Primary Navigation / Pages
Home
The home page will be primarily comprised of blog content. A layout and design is required for each of the following blog types:
• Standard – a typical weblog comprised of text and graphics
• Quote – a short snippet which includes a sentence and an attribution
• Video Blog – a video surrounded by
• Podcast
• Image – an image only (with caption) blog
Each blog post should contain social actions – the ability to tweet, share, etc. . .with the click of a button.
In addition to the core content, the home page should provide a brief introduction and standard picture and/or video. Other optional elements may include a tag cloud, search box, etc. . .use your creativity
About
Contains basic “about me” information. This page will serve as a template for all other “standard” pages. Please include the basic elements for a website in this page. These should include:
• A minimum of 3 Headings - H1, H2, and H3
• A bulleted list
• A numbered list
• A table
• An image
• A call to action (typically an image/button)
Boards
A special page dedicated to the boards I sit on and organizations I serve. There should be two sections – one for current board positions and one for previous positions. Each position should contain a logo, company name, and short description.
I imagine the organizations logo being in full color for the current positions but grey scale for the previous, but that’s just an idea, not a requirement.
Speaking
A special page dedicated to previous and upcoming speaking engagements. The layout may be similar to the Board page. No need to submit a separate layout for it unless you believe they should be different. Each speaking engagement will include a logo, event name, and short description as well as a date/time and whether it’s open to the public or not.
Contact
No need for a separate layout unless desired.
Other Elements
The Blog should provide quick access to the following blog “categories”:
• Business and Entrepreneurship
• Leadership and Inspiration
• Innovation and Technology
• Faith and Family
The template should include prominent links to each of my social media pages:
• Twitter
• LinkedIn
• YouTube
• Facebook
• Google+
The template should include a link to the blog archives

```html
<!DOCTYPE html>
<html lang="en">
<head>
<meta charset="utf-8">
<title>Marcus Thornbury | Quiet Resolve</title>
<link href="https://fonts.googleapis.com/css2?family=Open+Sans:wght@400;600;700;800&display=swap" rel="stylesheet">
<style>
:root{
  --blue:#1f7fc4;
  --blue-dark:#0f5f9e;
  --sky:#3da0e0;
  --orange:#f28a1e;
  --orange-dark:#d9700a;
  --green:#6cb33f;
  --text:#555;
  --muted:#8a8a8a;
  --line:#e2e2e2;
  --footer:#eeeeee;
  --white:#fff;
}
*{box-sizing:border-box;margin:0;padding:0}
html,body{width:742px;height:1200px;overflow:hidden;background:var(--white)}
body{font-family:"Open Sans",Arial,sans-serif;color:var(--text);font-size:9px;line-height:1.45;position:relative}
.page{position:relative;width:742px;height:1200px}

/* header */
.site-header{height:95px;display:flex;align-items:center;justify-content:space-between;padding:0 22px;border-bottom:1px solid var(--line)}
.brand{display:flex;align-items:center;gap:8px}
.brand-square{width:26px;height:26px;background:var(--blue)}
.brand-name{font-size:23px;font-weight:700;color:var(--blue);line-height:1}
.brand-tag{font-size:8px;font-weight:700;color:var(--blue);letter-spacing:2px;text-transform:uppercase;margin-top:3px}
.main-nav{display:flex;gap:3px;align-self:flex-start}
.main-nav a{display:block;padding:5px 11px 6px;font-size:9px;color:var(--white);background:var(--orange);text-decoration:none;border-radius:0 0 3px 3px}
.main-nav a.is-active{background:var(--orange-dark);font-weight:700}

/* hero */
.hero{position:relative;height:160px;background:linear-gradient(180deg,var(--blue-dark) 0%,var(--sky) 75%,#7cc36b 88%,var(--green) 100%);padding:16px 22px;color:var(--white);overflow:hidden}
.hero-title{font-size:19px;font-weight:800;letter-spacing:.3px;text-transform:uppercase}
.hero-text{width:430px;font-size:8.5px;margin-top:4px;line-height:1.4}
.hero-topics{display:flex;gap:6px;margin-top:12px}
.hero-topics a{background:var(--white);color:var(--blue);border:2px solid var(--green);border-radius:3px;padding:3px 9px;font-size:8.5px;font-weight:600;text-decoration:none}
.hero-portrait{position:absolute;right:40px;bottom:0;width:160px;height:150px;background:linear-gradient(180deg,#3b4c66,#1c2535);border-radius:70px 70px 0 0}

/* content */
.content{display:flex;gap:20px;padding:14px 22px 0}
.posts{width:438px}
.post{margin-bottom:22px}
.post-title{font-size:17px;font-weight:600;color:var(--blue);margin-bottom:4px}
.post-meta{display:flex;gap:14px;font-size:8px;color:var(--muted);border-top:1px solid var(--line);border-bottom:1px solid var(--line);padding:3px 0;margin-bottom:8px}
.post-body{display:flex;gap:12px}
.post-image{flex:0 0 178px;height:128px;border-radius:2px}
.img-bubbles{background:linear-gradient(135deg,#f3c23c,#6fb0e3 50%,#e35a4c)}
.img-people{background:linear-gradient(135deg,#d9dde2,#9fb3c8)}
.img-chart{background:linear-gradient(135deg,#f5f5f5,#c9d3dd)}
.post-excerpt p{font-size:8px;color:var(--text);margin-bottom:6px}
.read-more{display:inline-block;background:var(--orange);color:var(--white);font-size:7.5px;padding:2px 10px;border-radius:8px;text-decoration:none}

/* sidebar */
.sidebar{width:262px}
.search{display:flex;margin-bottom:12px}
.search-input{flex:1;border:1px solid #ccc;height:22px;font-size:8px;color:var(--muted);padding:5px 6px}
.search-btn{background:var(--orange);color:var(--white);font-size:9px;padding:4px 12px}
.photo{height:152px;margin-bottom:8px}
.photo-a{background:linear-gradient(180deg,#6aa7d8,#4f8f3a)}
.photo-b{background:linear-gradient(180deg,#c9d2dc,#7d8b99)}
.video{position:relative;height:138px;background:#111;margin-bottom:14px}
.video svg{position:absolute;left:50%;top:50%;transform:translate(-50%,-50%)}
.widget-title{font-size:16px;font-weight:600;color:var(--blue);border-bottom:1px solid var(--line);padding-bottom:3px;margin-bottom:6px}
.testimonial{font-size:8px}
.testimonial cite{display:block;text-align:right;font-style:normal;color:var(--blue);margin-top:4px}

/* footer */
.site-footer{position:absolute;left:0;top:920px;width:742px;height:250px;background:var(--footer);padding:14px 22px 0;border-top:3px solid var(--orange)}
.footer-cols{display:flex;gap:12px}
.footer-col{flex:1}
.footer-col h4{font-size:10px;color:#333;font-weight:700;margin-bottom:4px}
.footer-col ul{list-style:none}
.footer-col li{font-size:8px;color:var(--text);line-height:1.7}
.blog-item{display:flex;gap:5px;margin-bottom:6px}
.blog-thumb{flex:0 0 26px;height:22px;background:#b9c4cf}
.blog-item p{font-size:7px;line-height:1.3}
.blog-item b{font-size:8px;color:#333}
.footer-links{color:var(--orange)!important}
.footer-about{width:150px;margin-top:10px}
.footer-about p{font-size:7.5px}
.copyright{position:absolute;left:0;top:1170px;width:742px;height:30px;background:#dcdcdc;font-size:8px;color:var(--muted);text-align:right;padding:9px 22px}
</style>
</head>
<body>
<div class="page">
  <header class="site-header">
    <div class="brand">
      <span class="brand-square"></span>
      <div>
        <div class="brand-name">Marcus Thornbury</div>
        <div class="brand-tag">Quiet Resolve</div>
      </div>
    </div>
    <nav class="main-nav">
      <a href="#" class="is-active">Home</a>
      <a href="#">About Us</a>
      <a href="#">Reading List</a>
      <a href="#">Speaking</a>
      <a href="#">Archives</a>
      <a href="#">Contact</a>
    </nav>
  </header>

  <section class="hero">
    <h1 class="hero-title">Marcus Thornbury punch line here</h1>
    <p class="hero-text">We have learnt that designing is not only inclined to powerful imaginations but also focused and attentive to expected tastes. At a glance our work will make the best solutions appear simple, and we are glad to help clients who value clarity, craft and purpose every day.</p>
    <div class="hero-topics">
      <a href="#">Entrepreneurship</a>
      <a href="#">Leadership</a>
      <a href="#">Innovation</a>
      <a href="#">Faith and Family</a>
    </div>
    <div class="hero-portrait" role="img" aria-label="Portrait photo of Marcus Thornbury in a dark suit"></div>
  </section>

  <div class="content">
    <main class="posts">
      <article class="post">
        <h2 class="post-title">Communication Basics for the digital World</h2>
        <div class="post-meta"><span>576 Hits</span><span>27 Comments</span><span>Category – Leadership</span></div>
        <div class="post-body">
          <div class="post-image img-bubbles" role="img" aria-label="Illustration of colourful speech bubbles"></div>
          <div class="post-excerpt">
            <p>We have learnt that designing is not only inclined to powerful imaginations but also focused and attentive to expected tastes. Our team studies each brief with care and patience.</p>
            <p>Good solutions provide the best web designs which compel the customers to ask and inquire about the latest ideas and technologies for web design work.</p>
            <a href="#" class="read-more">Read more</a>
          </div>
        </div>
      </article>

      <article class="post">
        <h2 class="post-title">What is In a Name ?</h2>
        <div class="post-meta"><span>576 Hits</span><span>27 Comments</span><span>Category – Leadership</span></div>
        <div class="post-body">
          <div class="post-image img-people" role="img" aria-label="Photo of business people at a meeting"></div>
          <div class="post-excerpt">
            <p>We have learnt that designing is not only inclined to powerful imaginations but also focused and attentive to expected tastes. Our team studies each brief with care and patience.</p>
            <p>Good solutions provide the best web designs which compel the customers to ask and inquire about the latest ideas and technologies for web design work.</p>
            <a href="#" class="read-more">Read more</a>
          </div>
        </div>
      </article>

      <article class="post">
        <h2 class="post-title">Plan For Wild Success</h2>
        <div class="post-meta"><span>576 Hits</span><span>27 Comments</span><span>Category – Leadership</span></div>
        <div class="post-body">
          <div class="post-image img-chart" role="img" aria-label="Illustration of a growth plan on paper"></div>
          <div class="post-excerpt">
            <p>We have learnt that designing is not only inclined to powerful imaginations but also focused and attentive to expected tastes. Our team studies each brief with care and patience.</p>
            <a href="#" class="read-more">Read more</a>
          </div>
        </div>
      </article>
    </main>

    <aside class="sidebar">
      <div class="search"><span class="search-input">type your keyword here</span><span class="search-btn">Search</span></div>
      <div class="photo photo-a" role="img" aria-label="Photo of a speaker outdoors"></div>
      <div class="photo photo-b" role="img" aria-label="Photo of a speaking event audience"></div>
      <div class="video" role="img" aria-label="Video player">
        <svg width="34" height="34" viewBox="0 0 34 34"><circle cx="17" cy="17" r="16" fill="none" stroke="#fff" stroke-width="2"/><path d="M13 10 L25 17 L13 24 Z" fill="#fff"/></svg>
      </div>
      <h3 class="widget-title">Testimonials</h3>
      <div class="testimonial">
        <p>We have learnt that designing is not only inclined to powerful imaginations but also focused and attentive to expected tastes. Their work compels customers to ask and inquire about the latest technologies for web design, and we were happy with every result delivered.</p>
        <cite>– Client Name</cite>
      </div>
    </aside>
  </div>

  <footer class="site-footer">
    <div class="footer-cols">
      <div class="footer-col"><h4>Popular Topics</h4><ul><li>Dummy Text</li><li>Dummy Text</li><li>Dummy Text</li><li>Dummy Text</li><li>Dummy Text</li></ul></div>
      <div class="footer-col"><h4>Categories</h4><ul><li>Dummy Text</li><li>Dummy Text</li><li>Dummy Text</li><li>Dummy Text</li><li>Dummy Text</li></ul></div>
      <div class="footer-col"><h4>Blogs</h4>
        <div class="blog-item"><span class="blog-thumb"></span><p><b>Dummy Text</b><br>Lorem ipsum is simply dummy text</p></div>
        <div class="blog-item"><span class="blog-thumb"></span><p><b>Dummy Text</b><br>Lorem ipsum is simply dummy text</p></div>
        <div class="blog-item"><span class="blog-thumb"></span><p><b>Dummy Text</b><br>Lorem ipsum is simply dummy text</p></div>
      </div>
      <div class="footer-col"><h4>Quick Links</h4><ul><li>Dummy Text</li><li>Dummy Text</li><li>Dummy Text</li><li>Dummy Text</li><li>Dummy Text</li></ul></div>
      <div class="footer-col"><h4>Latest Blog</h4><ul><li>Dummy Text</li><li>Lorem ipsum is simply dummy</li><li>Dummy Text</li><li>Lorem ipsum is simply dummy</li><li class="footer-links">View All</li></ul></div>
    </div>
    <div class="footer-about">
      <h4 style="font-size:10px;color:#333">Topics</h4>
      <p>It is a long established fact that a reader will be distracted by the readable content of a page when looking at its layout. <span class="footer-links">Read more</span></p>
    </div>
  </footer>
  <div class="copyright">Copyright © 2012, All rights reserved</div>
</div>
</body>
</html>
```